The Lantern Protocol: A Practical Guide for Tending Old Orchards

This will be for both the hard cover and paperback version. A core theme of the book and what we want to cover to convey is the journey or transformation to "happiness". Concepts such as road/pathway, mountain top, sunrise, dark to bright colors, out-of-focus to in-focus, clouds parting, etc., all represent this idea. I am attaching a 1-page book summary for more information. I like the idea of the subtitle being in a gold seal, but that is not necessary. I am open to any designs, but it should at least be conceptually related to the book.

```html
<!DOCTYPE html>
<html lang="en">
<head>
<meta charset="utf-8">
<title>The Lantern Protocol — Cover Wrap</title>
<link rel="stylesheet" href="https://fonts.googleapis.com/css2?family=Oswald:wght@600;700&family=Montserrat:wght@400;500&family=Open+Sans:wght@400;600;700&display=swap">
<style>
  :root {
    --gold: #f7ac1f;
    --gold-deep: #b07a0c;
    --heading: #f2a516;
    --ink: #2b2b2b;
    --grey-type: #555555;
    --spine-grey: #6b6b6b;
    --paper: #ffffff;
    --tile-light: #eef0f2;
    --tile-mid: #c4c8cc;
    --tile-dark: #6f747a;
  }
  * { box-sizing: border-box; margin: 0; padding: 0; }
  html, body { width: 1200px; height: 873px; overflow: hidden; background: var(--paper); }
  .wrap { position: relative; width: 1200px; height: 873px; background: var(--paper); overflow: hidden; }

  /* Back cover */
  .back { position: absolute; left: 0; top: 0; width: 560px; height: 873px; }
  .back-title {
    position: absolute; top: 58px; left: 0; width: 584px; text-align: center;
    font-family: "Oswald", sans-serif; font-weight: 700; font-size: 29px;
    color: var(--gold); letter-spacing: 0; line-height: 1;
  }
  .back-subtitle {
    position: absolute; top: 98px; left: 0; width: 584px; text-align: center;
    font-family: "Montserrat", sans-serif; font-weight: 400; font-size: 14.5px;
    color: #111; letter-spacing: 0.3px;
  }
  .back-emblem {
    position: absolute; top: 124px; left: 278px; width: 40px; height: 26px;
    border-radius: 6px;
    background: radial-gradient(ellipse at 40% 40%, #ffd866, var(--gold) 55%, var(--gold-deep));
  }
  .back-copy {
    position: absolute; top: 160px; left: 61px; width: 468px;
    font-family: "Open Sans", sans-serif; font-size: 12.3px; line-height: 18.4px; color: var(--ink);
  }
  .back-copy h2 {
    font-family: "Open Sans", sans-serif; font-weight: 700; font-size: 13.5px;
    color: var(--heading); text-align: center; line-height: 20px; margin-bottom: 1px;
  }
  .back-copy p { margin: 0; }
  .back-copy .section { margin-bottom: 10px; }
  .back-copy ul { list-style: none; }
  .back-copy li { position: relative; padding-left: 11px; }
  .back-copy li::before {
    content: ""; position: absolute; left: 1px; top: 7px; width: 4px; height: 4px;
    border-radius: 50%; background: var(--heading);
  }
  .back-copy li.wrapped { padding-left: 11px; }

  /* Spine */
  .spine { position: absolute; left: 560px; top: 0; width: 64px; height: 873px; }
  .spine-author {
    position: absolute; left: 32px; top: 56px; transform-origin: 0 0; transform: rotate(90deg) translateY(-50%);
    white-space: nowrap; font-family: "Montserrat", sans-serif; font-weight: 500;
    font-size: 16.5px; letter-spacing: 1px; color: var(--spine-grey);
  }
  .spine-title {
    position: absolute; left: 32px; top: 260px; transform-origin: 0 0; transform: rotate(90deg) translateY(-50%);
    white-space: nowrap; font-family: "Oswald", sans-serif; font-weight: 700;
    font-size: 27px; letter-spacing: 0.5px; color: var(--gold);
  }
  .spine-emblem {
    position: absolute; left: 23px; top: 620px; width: 18px; height: 24px; border-radius: 4px;
    background: radial-gradient(ellipse at 40% 40%, #ffd866, var(--gold) 55%, var(--gold-deep));
  }

  /* Front cover */
  .front { position: absolute; left: 624px; top: 0; width: 576px; height: 873px; }
  .front-art {
    position: absolute; left: 0; top: 290px; width: 576px; height: 583px;
    background:
      radial-gradient(ellipse 55% 45% at 60% 52%, rgba(247,172,31,0.85), rgba(247,172,31,0) 70%),
      linear-gradient(170deg, var(--paper) 0%, var(--tile-light) 22%, var(--tile-mid) 60%, var(--tile-dark) 100%);
    -webkit-mask-image: linear-gradient(100deg, transparent 0%, #000 18%);
            mask-image: linear-gradient(100deg, transparent 0%, #000 18%);
  }
  .front-title {
    position: absolute; left: 40px; top: 50px; width: 510px; text-align: center;
    font-family: "Oswald", sans-serif; font-weight: 700; color: var(--gold);
    -webkit-text-stroke: 1.2px var(--gold-deep); line-height: 0.96;
  }
  .front-title .t-the { display: block; font-size: 46px; letter-spacing: 2px; }
  .front-title .t-main { display: block; font-size: 106px; letter-spacing: 1px; }
  .front-rule {
    position: absolute; left: 50px; top: 303px; width: 460px; height: 3px; background: var(--gold);
  }
  .front-subtitle {
    position: absolute; left: 30px; top: 314px; width: 520px; text-align: center;
    font-family: "Montserrat", sans-serif; font-weight: 400; font-size: 25px;
    line-height: 31px; color: var(--grey-type); letter-spacing: 0.5px;
  }
  .front-author {
    position: absolute; left: 40px; top: 778px; width: 500px; text-align: center;
    font-family: "Montserrat", sans-serif; font-weight: 500; font-size: 42px;
    color: var(--paper); letter-spacing: 0.5px;
    text-shadow: 0 2px 4px rgba(0,0,0,0.45);
  }
</style>
</head>
<body>
<div class="wrap">

  <section class="back">
    <h1 class="back-title">THE LANTERN PROTOCOL</h1>
    <p class="back-subtitle">A PRACTICAL GUIDE FOR TENDING OLD ORCHARDS</p>
    <div class="back-emblem" role="img" aria-label="Small golden puzzle piece emblem"></div>

    <div class="back-copy">
      <div class="section">
        <h2>Introduction:</h2>
        <p>"The Lantern Protocol" stems from a life-altering experience I had after nearly dying in a plane crash. This traumatic event led me to reconsider my life, my estate, and the beneficiaries. Instead of waiting until my death, I decided to give them the money immediately, allowing them to enjoy it and me to witness its impact. This concept of "pre-quests" became the foundation of my book.</p>
      </div>
      <div class="section">
        <h2>The Happiness Plan:</h2>
        <p>To ensure that the pre-quest funds were used effectively. The recipients included friends, family members, employees, and former employees. I asked each person to create a comprehensive "Happiness Plan."</p>
        <p>These plans were developed with the assistance of professional coaches, which I provided and focused on actionable steps to increase joy and fulfillment.</p>
        <p>The process involved:</p>
        <ul>
          <li>Identifying personal sources of happiness: Understanding what truly brings joy.</li>
          <li>Connecting our Virtues to our Values: Practicing the virtues that support our values.</li>
          <li>Forming Happiness Habits: Developing routines and practices to sustain long-term happiness.</li>
        </ul>
      </div>
      <div class="section">
        <h2>Real-World Results:</h2>
        <p>Each friend reported a significant increase in happiness. The book describes real-world examples of individuals working on their Happiness Plans, executing them, and observing the tangible benefits.</p>
        <p>Conclusion: "The Lantern Protocol" combines personal anecdotes and practical advice to offer a comprehensive guide for anyone seeking a happier, more fulfilling life.</p>
        <p>This book provides a new perspective on creating and sustaining joy in our lives and the lives of those we care about through prequests and Happiness Planning.</p>
      </div>
    </div>
  </section>

  <section class="spine">
    <span class="spine-author">MARTIN H. GREAVES</span>
    <span class="spine-title">THE LANTERN PROTOCOL</span>
    <div class="spine-emblem" role="img" aria-label="Small golden puzzle piece emblem"></div>
  </section>

  <section class="front">
    <div class="front-art" role="img" aria-label="Field of white jigsaw puzzle pieces with a glowing golden piece lifting out of its slot"></div>
    <h1 class="front-title">
      <span class="t-the">THE</span>
      <span class="t-main">LANTERN</span>
      <span class="t-main">PROTOCOL</span>
    </h1>
    <div class="front-rule"></div>
    <p class="front-subtitle">A PRACTICAL GUIDE FOR<br>TENDING OLD ORCHARDS</p>
    <p class="front-author">MARTIN H. GREAVES</p>
  </section>

</div>
</body>
</html>
```